Graphic Design for a Info Card

We would like a graphic design for an info card . We would like the colours to correspond to our logo , you can add in the colours navy blue or yellow if you would like. We would like it to have the following information. We want something that really pops. We would like the size to be 4 1/2 x 6 .

ATTENTION!! Delivery Promo! Order from us on the @hopplemeals app or @marlinrunner app on FRIDAYS and receive a FREE Sample of our one of our meal prep meals in your bag!
DID YOU KNOW?! Meal Prep is another great service that we offer. Saving you time, promoting your health, and best of all providing a delicious lunch . You can find more info on our website www.brivoranpantry.example . All orders are available for delivery or pickup!

```html
<!DOCTYPE html>
<html lang="en">
<head>
<meta charset="utf-8">
<title>Brivoran Info Card</title>
<link rel="stylesheet" href="https://fonts.googleapis.com/css2?family=Montserrat:wght@800&family=Great+Vibes&family=Arimo:wght@400;700&display=swap">
<style>
  :root {
    --lime: #95c23d;
    --ink: #060709;
    --white: #ffffff;
    --grey: #9b9b9b;
    --handle: #a3a3a3;
  }
  * { margin: 0; padding: 0; box-sizing: border-box; }
  html, body { width: 1085px; height: 1200px; overflow: hidden; }
  body { background: var(--lime); }
  .card {
    position: relative;
    width: 1085px;
    height: 1200px;
    background: var(--lime);
    font-family: "Arimo", Arial, sans-serif;
    overflow: hidden;
  }
  .splash {
    position: absolute;
    left: 60px;
    top: 150px;
    width: 976px;
    height: 980px;
  }
  .brand {
    position: absolute;
    left: 0;
    top: 18px;
    width: 100%;
    text-align: center;
  }
  .brand-name {
    font-family: "Montserrat", Arial, sans-serif;
    font-weight: 800;
    font-size: 88px;
    line-height: 90px;
    color: var(--ink);
    letter-spacing: 1px;
  }
  .brand-tagline {
    margin-top: 4px;
    font-family: "Montserrat", Arial, sans-serif;
    font-weight: 800;
    font-size: 26px;
    color: var(--white);
    letter-spacing: -0.5px;
  }
  .brand-tagline .divider { display: inline-block; margin: 0 12px; font-weight: 400; }
  .headline {
    position: absolute;
    left: 0;
    top: 250px;
    width: 100%;
    text-align: center;
    font-family: "Great Vibes", cursive;
    font-size: 112px;
    color: var(--white);
    padding-left: 10px;
  }
  .promo {
    position: absolute;
    left: 168px;
    top: 423px;
    width: 780px;
    font-size: 31px;
    line-height: 40.5px;
    color: var(--grey);
    letter-spacing: 0.3px;
  }
  .promo .handle { font-weight: 700; color: var(--handle); }
  .section-title {
    position: absolute;
    left: 0;
    top: 656px;
    width: 100%;
    text-align: center;
    font-weight: 700;
    font-size: 39px;
    letter-spacing: 3px;
    color: var(--white);
  }
  .about {
    position: absolute;
    left: 0;
    top: 740px;
    width: 1050px;
    text-align: center;
    font-size: 30px;
    line-height: 39.5px;
    letter-spacing: 2px;
    color: var(--grey);
  }
  .website {
    position: absolute;
    left: 0;
    top: 963px;
    width: 1045px;
    text-align: center;
    font-weight: 700;
    font-size: 29px;
    letter-spacing: 2.5px;
    color: var(--white);
  }
  .footer-note {
    position: absolute;
    left: 0;
    top: 1158px;
    width: 1085px;
    text-align: center;
    font-weight: 700;
    font-size: 30px;
    letter-spacing: 2.4px;
    color: var(--ink);
  }
</style>
</head>
<body>
<main class="card">
  <svg class="splash" viewBox="0 0 976 980" role="img" aria-label="Black paint brush splash with grey streaks behind the card text">
    <defs>
      <radialGradient id="splashFill" cx="50%" cy="48%" r="55%">
        <stop offset="0%" stop-color="#060709"/>
        <stop offset="78%" stop-color="#0a0a0c"/>
        <stop offset="92%" stop-color="#3a3b3a" stop-opacity="0.8"/>
        <stop offset="100%" stop-color="#95c23d" stop-opacity="0"/>
      </radialGradient>
    </defs>
    <ellipse cx="488" cy="490" rx="500" ry="505" fill="url(#splashFill)"/>
  </svg>

  <header class="brand">
    <div class="brand-name">BRIVORAN</div>
    <div class="brand-tagline">HEALTHY KITCHEN<span class="divider">|</span>MEAL PREP</div>
  </header>

  <h1 class="headline">Attention!!</h1>

  <p class="promo">Delivery Promo! Order from us on the <span class="handle">@hopplemeals</span> app or <span class="handle">@marlinrunner</span> app on FRIDAYS and receive a FREE Sample of our one of our meal prep meals in your bag!</p>

  <h2 class="section-title">DID YOU KNOW?!</h2>

  <p class="about">Meal Prep is another great service<br>that we offer. Saving you time, promoting<br>your health, and best of all providing<br>a delicious lunch . You can find<br>more info on our website</p>

  <p class="website">www.brivoranpantry.example</p>

  <p class="footer-note">All orders are available for delivery or pickup!</p>
</main>
</body>
</html>
```